Bref créative
Sendero alba Business Cards and Stationery
Sendero A.L.B.A.
Professional
Rodrigo Tamborel
Pastor Asociado
318 Conway Ave
Birchvale NJ 07952
pastor_rodrigo@senderoalba.org
www.senderoalba.org
Please use below link to download Logo vector files: http://fx.qk/Tz8RwLp2Hn

```html
<!DOCTYPE html>
<html lang="en">
<head>
<meta charset="utf-8">
<title>Sendero alba — Stationery Set</title>
<link href="https://fonts.googleapis.com/css2?family=Montserrat:wght@400;600;700&display=swap" rel="stylesheet">
<style>
  :root{
    --backdrop:#e4e4e4;
    --paper:#ffffff;
    --navy:#1c3b68;
    --navy-deep:#10264a;
    --navy-soft:#2f5487;
    --gold:#e9a228;
    --ink:#4a4f57;
    --rule:#c9ced6;
  }
  *{box-sizing:border-box;margin:0;padding:0}
  html,body{width:1200px;height:336px;overflow:hidden;background:var(--backdrop);font-family:"Montserrat",sans-serif;color:var(--ink)}
  .set{position:relative;width:1200px;height:336px}
  .piece{position:absolute;background:var(--paper);box-shadow:0 1px 3px rgba(0,0,0,.25);overflow:hidden}
  .wave{position:absolute;left:0;bottom:0;width:100%;display:block}
  .brand{position:absolute;display:flex;align-items:center;gap:4px;font-weight:700;color:var(--navy);white-space:nowrap}
  .brand-mark{background:var(--gold);flex:none}
  .contact{position:absolute;font-size:3.4px;line-height:1.4;text-align:right;color:var(--ink);white-space:nowrap}

  /* business cards */
  .card{width:56px;height:34px}
  .card-front{left:12px;top:144px}
  .card-back{left:12px;top:190px}
  .card .brand{font-size:5px;gap:2px}
  .card .brand-mark{width:4px;height:4px}
  .card-back .brand{left:5px;top:6px}
  .card-front .brand{left:50%;top:9px;transform:translateX(-50%)}
  .card-back .contact{left:5px;top:14px;text-align:left;font-size:2.4px}

  /* letterheads */
  .letter{width:142px;height:296px;top:12px}
  .letter-a{left:100px}
  .letter-b{left:276px}
  .letter .brand{left:10px;top:10px;font-size:8px}
  .letter .brand-mark{width:6px;height:6px}
  .letter .contact{right:10px;top:10px}
  .invoice-title{position:absolute;left:10px;top:36px;font-size:5px;font-weight:700;color:var(--navy)}
  .invoice-table{position:absolute;left:10px;top:44px;width:122px;border-collapse:collapse;font-size:3.4px}
  .invoice-table th,.invoice-table td{border:.5px solid var(--rule);height:7px;padding:0 2px;text-align:left;font-weight:600}

  /* envelopes */
  .envelope{width:122px;height:118px;left:440px}
  .envelope-front{top:12px}
  .envelope-back{top:144px}
  .envelope-front .brand{left:8px;top:8px;font-size:7px}
  .envelope-front .brand-mark{width:5px;height:5px}
  .flap{position:absolute;left:0;top:0;width:100%;height:70px}

  /* compliment slip */
  .slip{left:444px;top:283px;width:118px;height:30px}
  .slip .brand{left:6px;top:5px;font-size:5px;gap:2px}
  .slip .brand-mark{width:4px;height:4px}
  .slip .contact{right:6px;top:5px;font-size:2.8px}

  /* presentation folder */
  .folder{left:628px;top:12px;width:562px;height:312px;background:none;box-shadow:none;overflow:visible}
  .folder-back{position:absolute;left:0;top:0;width:250px;height:312px;background:linear-gradient(160deg,var(--navy-soft),var(--navy-deep));box-shadow:0 1px 3px rgba(0,0,0,.3)}
  .folder-back-pocket{position:absolute;left:0;bottom:0;width:100%;height:110px;border-top:1px solid rgba(255,255,255,.15);background:rgba(0,0,0,.12)}
  .folder-front{position:absolute;left:250px;top:0;width:312px;height:312px;background:var(--paper);box-shadow:0 1px 3px rgba(0,0,0,.3);overflow:hidden}
  .folder-front .brand{left:50%;top:112px;transform:translateX(-50%);font-size:20px;gap:8px}
  .folder-front .brand-mark{width:16px;height:16px}
</style>
</head>
<body>
<main class="set">

  <section class="piece card card-front" aria-label="Business card front">
    <div class="brand"><span class="brand-mark"></span>Sendero alba</div>
    <svg class="wave" viewBox="0 0 100 30" preserveAspectRatio="none" height="14">
      <path d="M0 12 Q50 0 100 10 L100 30 L0 30Z" fill="var(--gold)"/>
      <path d="M0 16 Q50 4 100 14 L100 30 L0 30Z" fill="var(--navy)"/>
    </svg>
  </section>

  <section class="piece card card-back" aria-label="Business card back">
    <div class="brand"><span class="brand-mark"></span>Sendero alba</div>
    <div class="contact">Rodrigo Tamborel · Pastor Asociado<br>318 Conway Ave, Birchvale NJ 07952<br>pastor_rodrigo@senderoalba.org</div>
    <svg class="wave" viewBox="0 0 100 30" preserveAspectRatio="none" height="6">
      <path d="M0 14 Q50 2 100 12 L100 30 L0 30Z" fill="var(--gold)"/>
      <path d="M0 18 Q50 6 100 16 L100 30 L0 30Z" fill="var(--navy)"/>
    </svg>
  </section>

  <section class="piece letter letter-a" aria-label="Letterhead">
    <div class="brand"><span class="brand-mark"></span>Sendero alba</div>
    <div class="contact">318 Conway Ave<br>Birchvale NJ 07952<br>pastor_rodrigo@senderoalba.org<br>www.senderoalba.org</div>
    <svg class="wave" viewBox="0 0 100 30" preserveAspectRatio="none" height="40">
      <path d="M0 14 Q35 2 60 10 T100 6 L100 30 L0 30Z" fill="var(--gold)"/>
      <path d="M0 18 Q35 6 60 14 T100 10 L100 30 L0 30Z" fill="var(--navy)"/>
    </svg>
  </section>

  <section class="piece letter letter-b" aria-label="Letterhead with form">
    <div class="brand"><span class="brand-mark"></span>Sendero alba</div>
    <div class="contact">318 Conway Ave<br>Birchvale NJ 07952<br>pastor_rodrigo@senderoalba.org<br>www.senderoalba.org</div>
    <p class="invoice-title">Invoice</p>
    <table class="invoice-table">
      <tr><th>Date</th><th>Item</th><th>Qty</th><th>Total</th></tr>
      <tr><td></td><td></td><td></td><td></td></tr>
      <tr><td></td><td></td><td></td><td></td></tr>
      <tr><td></td><td></td><td></td><td></td></tr>
    </table>
    <svg class="wave" viewBox="0 0 100 30" preserveAspectRatio="none" height="40">
      <path d="M0 14 Q35 2 60 10 T100 6 L100 30 L0 30Z" fill="var(--gold)"/>
      <path d="M0 18 Q35 6 60 14 T100 10 L100 30 L0 30Z" fill="var(--navy)"/>
    </svg>
  </section>

  <section class="piece envelope envelope-front" aria-label="Envelope front">
    <div class="brand"><span class="brand-mark"></span>Sendero alba</div>
    <svg class="wave" viewBox="0 0 100 30" preserveAspectRatio="none" height="26">
      <path d="M0 14 Q40 2 100 10 L100 30 L0 30Z" fill="var(--gold)"/>
      <path d="M0 18 Q40 6 100 14 L100 30 L0 30Z" fill="var(--navy)"/>
    </svg>
  </section>

  <section class="piece envelope envelope-back" aria-label="Envelope back">
    <svg class="flap" viewBox="0 0 100 60" preserveAspectRatio="none">
      <path d="M0 0 L100 0 L50 58Z" fill="#f4f5f7" stroke="var(--rule)" stroke-width=".6"/>
    </svg>
  </section>

  <section class="piece slip" aria-label="Compliment slip">
    <div class="brand"><span class="brand-mark"></span>Sendero alba</div>
    <div class="contact">318 Conway Ave<br>www.senderoalba.org</div>
    <svg class="wave" viewBox="0 0 100 30" preserveAspectRatio="none" height="8">
      <path d="M0 14 Q50 2 100 12 L100 30 L0 30Z" fill="var(--gold)"/>
      <path d="M0 18 Q50 6 100 16 L100 30 L0 30Z" fill="var(--navy)"/>
    </svg>
  </section>

  <section class="piece folder" aria-label="Presentation folder">
    <div class="folder-back">
      <div class="folder-back-pocket"></div>
    </div>
    <div class="folder-front">
      <div class="brand"><span class="brand-mark"></span>Sendero alba</div>
      <svg class="wave" viewBox="0 0 100 30" preserveAspectRatio="none" height="90">
        <path d="M0 10 Q45 0 100 8 L100 30 L0 30Z" fill="var(--gold)"/>
        <path d="M0 13 Q45 3 100 11 L100 30 L0 30Z" fill="var(--navy)"/>
      </svg>
    </div>
  </section>

</main>
</body>
</html>
```